A WEBSITE FOR A JEWELLERY RETAIL STORE WITH A SHOPPING CART, AND ABILITY TO ORDER ONLINE.

I require a website with a shopping cart.

We sell MAINLY diamond jewellery (such as rings etc). I need it to be simple to change prices with only a few buttons, as the price fluctuates due to the US Dollar.

We are a diamond wholesaler, selling directly to the public, so we guarantee the lowest prices in Australia.

There is also a link to current inventory that will need to be uploaded to the site.

This could be an ongoing job, where you will be paid weekly to maintain and update the website if you wish.

Target Market(s)

People getting engaged, and wanting to buy a diamond ring.

Number of Pages Required

5+ page

Colors

Designer to choose colors to be used in the design.

Requirements
Must have
• elegant.
• modern.
• professional.
• SHOPPING CART.
• ABILITY TO SEARCH FOR LOOSE DIAMONDS (LINK THAT NEEDS TO BE EMBEDDED WILL BE SENT WHICH SHOWS CURRENT STOCK).
• ENGAGEMENT RINGS
• WEDDING RINGS
• DIAMOND EARRINGS
• DIAMOND PENDANTS
• LOOSE DIAMONDS.
• SALE ITEMS.
• OTHER JEWELLERY.
• EDUCATION
• WISH LIST
• CART.
Nice to have
• a good place to look for inspiration on pages is https://www.velmarigems.example.
• YOU MAY VISIT OUR FACEBOOK PAGE AT.
• HTTP://WWW.SOCIALPAGE.EXAMPLE/QUINTORAJEWELLERS
Should not have
• We don't want it too busy.

```html
<!DOCTYPE html>
<html lang="en">
<head>
<meta charset="utf-8">
<title>Quintora Jewellers</title>
<link rel="stylesheet" href="https://fonts.googleapis.com/css2?family=Oranienbaum&family=Lato:ital,wght@0,400;0,700;1,400&display=swap">
<style>
:root{
  --mauve:#9a6366;
  --mauve-dark:#7b4b4f;
  --mauve-deep:#6e4145;
  --blush:#f7cbc8;
  --blush-light:#fcefee;
  --text:#4a3a3b;
  --muted:#8c7a7b;
  --white:#ffffff;
  --line:#e8d6d5;
  --silver-hi:#f7f7f8;
  --silver-lo:#cfd0d3;
  --gold-hi:#f8f0da;
  --gold-lo:#d6b86c;
}
*{box-sizing:border-box;margin:0;padding:0}
html,body{width:1200px;height:3797px;overflow:hidden}
body{font-family:"Lato",sans-serif;color:var(--text);background:var(--white);position:relative}
a{color:inherit;text-decoration:none}

/* header */
.topbar{position:absolute;top:0;left:0;width:1200px;height:110px;background:var(--white)}
.social{position:absolute;left:78px;top:36px;display:flex;gap:8px}
.social span{width:34px;height:34px;background:var(--mauve);display:block}
.brand{position:absolute;left:470px;top:22px;display:flex;align-items:center;gap:12px}
.brand-mark{width:26px;height:26px;background:var(--blush)}
.brand-name{font-family:"Oranienbaum",serif;font-size:40px;letter-spacing:3px;color:var(--mauve)}
.brand-sub{position:absolute;left:508px;top:68px;font-family:"Oranienbaum",serif;font-size:15px;letter-spacing:7px;color:var(--mauve)}
.account{position:absolute;right:78px;top:42px;display:flex;align-items:center;gap:28px;font-size:13px;letter-spacing:1px;color:var(--muted)}
.cart-count{display:inline-block;width:20px;height:20px;border-radius:50%;background:var(--mauve);color:#fff;font-size:11px;text-align:center;line-height:20px;margin-left:4px;vertical-align:top}
.flag{width:40px;height:24px;background:linear-gradient(#b33 0 50%,#eee 50%);border:1px solid #ccc}

.nav{position:absolute;top:110px;left:0;width:1200px;height:67px;background:var(--blush-light);border-top:1px solid var(--line);border-bottom:1px solid var(--line);display:flex;align-items:center;padding-left:122px;gap:38px;font-size:14px;letter-spacing:1px;color:var(--mauve-dark)}
.nav span::before{content:"◇";margin-right:10px;color:var(--mauve)}
.nav .search{position:absolute;left:1055px;top:20px}

/* hero */
.hero{position:absolute;top:177px;left:0;width:1200px;height:575px;overflow:hidden}
.hero-bg{position:absolute;inset:0;background:linear-gradient(90deg,#f1f1f2 0%,#ebebec 40%,#e4e2e3 100%)}
.hero-photo{position:absolute;left:560px;top:0;width:640px;height:575px;
  background:
    radial-gradient(ellipse 120px 90px at 330px 390px,rgba(222,150,110,.55),rgba(222,150,110,0) 100%),
    radial-gradient(ellipse 260px 330px at 420px 140px,#f6ecea 0%,#efe3e1 45%,rgba(239,227,225,0) 100%),
    radial-gradient(ellipse 200px 260px at 360px 420px,#f3e8e6 0%,rgba(243,232,230,0) 100%),
    linear-gradient(90deg,rgba(236,236,237,0) 0%,#e7e2e2 45%,#d9d3d4 100%)}
.hero-copy{position:absolute;left:78px;top:160px}
.hero-copy h1{font-family:"Oranienbaum",serif;font-weight:400;font-size:46px;line-height:62px;color:var(--mauve-dark);letter-spacing:1px}
.hero-copy p{font-size:17px;font-style:italic;color:#333;margin-top:12px}
.btn{display:inline-block;height:50px;line-height:50px;padding:0 30px;border-radius:25px;font-size:14px;letter-spacing:1px;text-align:center}
.btn-dark{background:var(--mauve-dark);color:#fff;box-shadow:0 3px 0 #5b3538}
.btn-light{background:var(--blush);color:var(--mauve-dark);box-shadow:0 3px 0 #e2aaa6}
.hero-actions{margin-top:26px;display:flex;gap:20px}
.dots{position:absolute;left:560px;top:494px;display:flex;gap:14px}
.dots span{width:18px;height:18px;border-radius:50%;border:2px solid var(--mauve);background:#fff}
.dots span:first-child{background:var(--mauve)}

.promo{position:absolute;top:752px;left:0;width:1200px;height:81px;background:var(--mauve);color:#fff;font-size:19px;letter-spacing:1px;text-align:center;line-height:81px}

/* categories */
.categories{position:absolute;top:833px;left:0;width:1200px;height:887px;background:#fff}
.cat-card{position:absolute;background:linear-gradient(135deg,var(--blush-light),#c9a3a4)}
.cat-card h3{font-family:"Oranienbaum",serif;font-weight:400;font-size:28px;color:var(--mauve-dark);margin-bottom:14px}
.cat-card p{font-size:13px;line-height:24px;color:#3d3333}
.cat-frame{position:absolute;border:2px solid var(--mauve-deep)}
.cat-photo{position:absolute;border-radius:6px}
.cat-photo.silver{background:linear-gradient(160deg,var(--silver-hi) 10%,#dcdcde 55%,var(--silver-lo))}
.cat-photo.mixed{background:linear-gradient(160deg,#f5f2ee 10%,#dcc9a8 55%,#c6c6c9)}
.cat-photo.gold{background:linear-gradient(160deg,var(--gold-hi) 10%,#e3cc8e 55%,var(--gold-lo))}

/* custom band */
.design{position:absolute;top:1720px;left:0;width:1200px;height:335px;text-align:center}
.design-photo{position:absolute;inset:0;background:
  radial-gradient(ellipse 300px 160px at 900px 200px,#f8eeed,rgba(248,238,237,0)),
  linear-gradient(90deg,#e4c6c5,#f4e4e3 50%,#e3c4c3)}
.design-copy{position:relative}
.design h2{font-family:"Oranienbaum",serif;font-weight:400;font-size:38px;color:#fff;padding-top:58px;text-shadow:0 1px 3px rgba(110,65,69,.35)}
.design p{font-size:17px;font-style:italic;line-height:28px;color:#2e2424;margin-top:14px}
.design .btn{margin-top:26px}

/* loose diamonds */
.loose{position:absolute;top:2055px;left:0;width:1200px;height:526px;text-align:center}
.loose h2{font-family:"Oranienbaum",serif;font-weight:400;font-size:42px;color:var(--mauve-dark);margin-top:60px}
.loose .lead{font-size:17px;font-style:italic;line-height:32px;color:var(--muted);margin:24px auto 0;width:640px}
.shape{position:absolute;top:2290px;width:110px;margin-left:-55px;text-align:center;font-size:14px;letter-spacing:1px;color:var(--mauve-dark)}
.shape svg{display:block;margin:0 auto 14px}
.shape.active{top:2270px}
.shape.active .frame{width:110px;height:110px;border:3px solid #f0dddc;border-radius:14px;background:#fff;display:flex;align-items:center;justify-content:center;margin:0 auto 10px;box-shadow:0 2px 6px rgba(0,0,0,.08)}
.shape.active .frame svg{margin:0}
.arrow{position:absolute;top:2310px}

/* press */
.press{position:absolute;top:2585px;left:0;width:1200px;height:105px;border-top:1px solid var(--line);border-bottom:1px solid var(--line);display:flex;align-items:center;justify-content:space-around;padding:0 80px}
.press span{display:block;background:#d9d0d0;border-radius:8px;height:40px}

/* featured */
.featured{position:absolute;top:2690px;left:0;width:1200px;height:676px;text-align:center}
.featured h2{font-family:"Oranienbaum",serif;font-weight:400;font-size:42px;color:var(--mauve-dark);margin-top:60px}
.product{position:absolute;top:2834px;width:241px;height:366px;background:linear-gradient(180deg,#fbe9e8,#ad7c7e);text-align:center}
.product .img{width:183px;height:180px;margin:30px auto 0;background:#fff;border:2px solid #f3e0df;padding:12px}
.product .shot{width:100%;height:100%}
.product .shot.silver{background:linear-gradient(165deg,#fbfbfb 0%,#ececee 40%,#d3d4d7 100%)}
.product .shot.gold{background:linear-gradient(165deg,#fdfaf1 0%,#f1e3bb 40%,#d9bd72 100%)}
.product h4{font-weight:400;font-size:17px;color:#2b2222;margin-top:30px}
.product .price{font-size:24px;color:var(--mauve-dark);margin-top:10px;letter-spacing:1px}
.product .buy{display:inline-block;font-size:13px;font-weight:700;color:#2b2222;border-bottom:1px solid #2b2222;margin-top:12px}
.f-arrow{position:absolute;top:3010px}
.view-all{position:absolute;top:3254px;left:497px}

/* footer */
.footer{position:absolute;top:3366px;left:0;width:1200px;height:367px;background:var(--mauve);color:#fff}
.col{position:absolute;top:58px}
.col h5{font-family:"Oranienbaum",serif;font-weight:400;font-size:22px;margin-bottom:20px}
.col li{list-style:none;font-size:13px;line-height:25px}
.contact li b{display:inline-block;width:30px}
.hours{margin-top:20px}
.col .note{font-size:13px;line-height:21px;width:240px}
.email{width:240px;height:50px;background:#fff;border-radius:25px;margin-top:16px;display:flex;align-items:center;padding-left:24px;gap:14px;color:var(--muted);font-size:14px}
.subscribe{margin-top:16px;background:var(--blush);color:var(--mauve-dark);height:48px;line-height:48px;padding:0 26px;font-size:15px}
.bottombar{position:absolute;top:3733px;left:0;width:1200px;height:64px;background:var(--mauve-deep);color:#fff;font-size:13px;display:flex;align-items:center;padding:0 78px}
.bottombar .icons{margin-left:auto;display:flex;gap:8px}
.bottombar .icons span{width:34px;height:34px;background:var(--blush);opacity:.9}
.bottombar .icons span:first-child{background:#f6b8b4}
</style>
</head>
<body>

<header class="topbar">
  <div class="social" aria-label="Social links"><span></span><span></span><span></span><span></span><span></span></div>
  <div class="brand"><span class="brand-mark"></span><span class="brand-name">QUINTORA</span></div>
  <div class="brand-sub">JEWELLERS</div>
  <div class="account">
    <span>WHISHLIST</span><span>LOGIN</span>
    <span>CART
      <svg width="20" height="18" viewBox="0 0 20 18" style="vertical-align:middle;margin-left:6px"><path d="M1 2h3l2 10h10l2-7H6" fill="none" stroke="#555" stroke-width="2"/><circle cx="8" cy="15.5" r="1.6" fill="#555"/><circle cx="15" cy="15.5" r="1.6" fill="#555"/></svg><span class="cart-count">0</span></span>
    <span class="flag" role="img" aria-label="Country selector"></span>
  </div>
</header>

<nav class="nav">
  <span>DIAMONDS</span><span>ENGAGEMENT RINGS</span><span>WEDDING</span><span>JEWELRY</span><span>EDUCATION</span><span>ON SALE</span>
  <svg class="search" width="24" height="24" viewBox="0 0 24 24"><circle cx="10" cy="10" r="7" fill="none" stroke="#9a8586" stroke-width="2"/><path d="M15 15l6 6" stroke="#9a8586" stroke-width="2"/></svg>
</nav>

<section class="hero">
  <div class="hero-bg"></div>
  <div class="hero-photo" role="img" aria-label="Soft-lit portrait of a woman resting her hand at her chin, wearing a rose gold diamond ring"></div>
  <div class="hero-copy">
    <h1>YOU DESIGN IT WE BUILD IT<br>SHE SAYS YES</h1>
    <p>Create your own unique diamond engagement ring.</p>
    <div class="hero-actions"><a class="btn btn-dark">ENGAGEMENT RINGS</a><a class="btn btn-light">LOOSE DIAMONDS</a></div>
  </div>
  <div class="dots"><span></span><span></span><span></span></div>
</section>

<div class="promo">ORDER NOW AND ENJOY FREE SWIFTPOST® OVERNIGHT SHIPPING AND 30-DAY RETURNS</div>

<section class="categories">
  <div class="cat-card" style="left:94px;top:65px;width:433px;height:259px;padding:58px 0 0 22px">
    <h3>Engagement Rings</h3>
    <p>Lorem ipsum dolor sit amet, sed do<br>eiusmod tempor incididunt ut labore<br>et dolore magna aliqua.</p>
  </div>
  <div class="cat-frame" style="left:382px;top:116px;width:238px;height:158px"></div>
  <div class="cat-photo mixed" role="img" aria-label="Stacked gold and white gold diamond rings" style="left:418px;top:88px;width:168px;height:158px"></div>

  <div class="cat-card" style="left:665px;top:118px;width:334px;height:240px;padding:30px 0 0 54px">
    <h3>Diamond Earrings</h3>
    <p>Lorem ipsum dolor sit amet, sed do<br>eiusmod tempor incididunt ut labore<br>et dolore magna aliqua.</p>
  </div>
  <div class="cat-frame" style="left:736px;top:305px;width:192px;height:190px"></div>
  <div class="cat-photo silver" role="img" aria-label="Pair of round diamond stud earrings" style="left:718px;top:300px;width:170px;height:150px"></div>

  <div class="cat-frame" style="left:228px;top:381px;width:189px;height:185px"></div>
  <div class="cat-photo silver" role="img" aria-label="Diamond circle pendant with red butterflies on a fine chain" style="left:262px;top:346px;width:122px;height:200px"></div>
  <div class="cat-card" style="left:157px;top:470px;width:331px;height:329px;padding:150px 0 0 50px">
    <h3>Diamond Pandents</h3>
    <p>Lorem ipsum dolor sit amet, sed do<br>eiusmod tempor incididunt ut labore<br>et dolore magna aliqua.</p>
  </div>

  <div class="cat-card" style="left:670px;top:553px;width:436px;height:259px;padding:60px 0 0 170px">
    <h3>Wedding Rings</h3>
    <p>Lorem ipsum dolor sit amet, sed do<br>eiusmod tempor incididunt ut labore<br>et dolore magna aliqua.</p>
  </div>
  <div class="cat-frame" style="left:546px;top:601px;width:266px;height:160px"></div>
  <div class="cat-photo gold" role="img" aria-label="Pair of gold wedding bands" style="left:531px;top:630px;width:230px;height:110px"></div>
</section>

<section class="design">
  <div class="design-photo" role="img" aria-label="Soft blurred photo of rings resting on pink fabric"></div>
  <div class="design-copy">
    <h2>You Design It, We Build It</h2>
    <p>Make it your own. Each ring is a one of a kind masterpiece made for you<br>in our Los Angeles manufacturing house.</p>
    <a class="btn btn-dark">DESIGN YOUR OWN RING</a>
  </div>
</section>

<section class="loose">
  <h2>Loose Diamonds</h2>
  <p class="lead">Search nearly 150,000 GLC and DGS certified loose diamonds. Our Diamond Search tool allows you to filter by the 4 C's and more!</p>
  <a class="btn btn-light" style="position:absolute;left:466px;top:415px;padding:0 26px;height:46px;line-height:46px">SEARCH LOOSE DIAMONDS</a>
</section>

<svg class="arrow" style="left:58px" width="20" height="60" viewBox="0 0 20 60"><path d="M17 2L3 30l14 28" fill="none" stroke="#999" stroke-width="2"/></svg>
<svg class="arrow" style="left:1122px" width="20" height="60" viewBox="0 0 20 60"><path d="M3 2l14 28L3 58" fill="none" stroke="#999" stroke-width="2"/></svg>

<div class="shape" style="left:127px"><svg width="64" height="64" viewBox="0 0 64 64" fill="none" stroke="#9a6366" stroke-width="1.5"><circle cx="32" cy="32" r="29"/><circle cx="32" cy="32" r="15"/><path d="M32 3v14M32 47v14M3 32h14M47 32h14M12 12l10 10M42 42l10 10M52 12L42 22M22 42L12 52"/></svg>ROUND</div>
<div class="shape" style="left:240px"><svg width="64" height="64" viewBox="0 0 64 64" fill="none" stroke="#9a6366" stroke-width="1.5"><rect x="4" y="4" width="56" height="56"/><rect x="16" y="16" width="32" height="32"/><path d="M4 4l56 56M60 4L4 60"/></svg>PRINCESS</div>
<div class="shape" style="left:357px"><svg width="40" height="64" viewBox="0 0 40 64" fill="none" stroke="#9a6366" stroke-width="1.5"><rect x="4" y="3" width="32" height="58" rx="6"/><rect x="11" y="12" width="18" height="40"/></svg>MARQUISE</div>
<div class="shape" style="left:471px"><svg width="64" height="64" viewBox="0 0 64 64" fill="none" stroke="#9a6366" stroke-width="1.5"><path d="M12 4h40l8 8v40l-8 8H12l-8-8V12z"/><rect x="16" y="16" width="32" height="32"/></svg>EMERALD</div>
<div class="shape active" style="left:600px"><div class="frame"><svg width="84" height="56" viewBox="0 0 84 56"><path d="M4 28C20 6 60 4 80 28 60 52 20 50 4 28z" fill="#b27f82" stroke="#6e4145" stroke-width="2"/><path d="M4 28h76M24 12l18 16-18 16M60 12L42 28l18 16" fill="none" stroke="#6e4145" stroke-width="1.5"/></svg></div><span style="font-size:16px">PEAR</span></div>
<div class="shape" style="left:729px"><svg width="40" height="64" viewBox="0 0 40 64" fill="none" stroke="#9a6366" stroke-width="1.5"><path d="M10 3h20l6 6v46l-6 6H10l-6-6V9z"/><rect x="12" y="14" width="16" height="36"/></svg>OVAL</div>
<div class="shape" style="left:843px"><svg width="44" height="64" viewBox="0 0 44 64" fill="none" stroke="#9a6366" stroke-width="1.5"><ellipse cx="22" cy="32" rx="19" ry="29"/><ellipse cx="22" cy="32" rx="9" ry="15"/><path d="M22 3v14M22 47v14M3 32h10M31 32h10"/></svg>HEART</div>
<div class="shape" style="left:956px"><svg width="44" height="64" viewBox="0 0 44 64" fill="none" stroke="#9a6366" stroke-width="1.5"><path d="M22 3C36 22 41 34 41 42a19 19 0 0 1-38 0c0-8 5-20 19-39z"/><path d="M22 3v56M8 38h28"/></svg>RADIANT</div>
<div class="shape" style="left:1070px"><svg width="64" height="60" viewBox="0 0 64 60" fill="none" stroke="#9a6366" stroke-width="1.5"><path d="M32 57L5 28C-2 18 4 4 17 4c7 0 12 5 15 10 3-5 8-10 15-10 13 0 19 14 12 24z"/><path d="M32 14v43M10 24l22 8 22-8"/></svg>ASSCHER</div>

<div class="press" aria-label="As featured in">
  <span style="width:150px"></span><span style="width:190px"></span><span style="width:70px"></span><span style="width:110px"></span><span style="width:260px"></span>
</div>

<section class="featured"><h2>Featured products</h2></section>

<svg class="f-arrow" style="left:52px" width="14" height="22" viewBox="0 0 14 22"><path d="M12 2L3 11l9 9" fill="none" stroke="#333" stroke-width="3"/></svg>
<svg class="f-arrow" style="left:1136px" width="14" height="22" viewBox="0 0 14 22"><path d="M2 2l9 9-9 9" fill="none" stroke="#111" stroke-width="3"/></svg>

<div class="product" style="left:78px"><div class="img"><div class="shot silver" role="img" aria-label="Marquise diamond halo engagement ring in white gold"></div></div><h4>Engagement Ring</h4><div class="price">$ 325.00</div><a class="buy">BUY NOW</a></div>
<div class="product" style="left:344px"><div class="img"><div class="shot gold" role="img" aria-label="Round diamond double halo ring in yellow gold"></div></div><h4>Marrige Ring</h4><div class="price">$ 325.00</div><a class="buy">BUY NOW</a></div>
<div class="product" style="left:612px"><div class="img"><div class="shot silver" role="img" aria-label="Oval diamond halo engagement ring in white gold"></div></div><h4>Engagement Ring</h4><div class="price">$ 325.00</div><a class="buy">BUY NOW</a></div>
<div class="product" style="left:880px"><div class="img"><div class="shot gold" role="img" aria-label="Round diamond halo ring in yellow gold"></div></div><h4>Marrige Ring</h4><div class="price">$ 325.00</div><a class="buy">BUY NOW</a></div>

<a class="btn btn-dark view-all" style="height:46px;line-height:46px;padding:0 26px">VIEW ALL PRODUCTS</a>

<footer class="footer">
  <div class="col" style="left:78px"><h5>Categories</h5><ul><li>Collections</li><li>About us</li><li>Contact us</li><li>Blog</li><li>Sitemap</li><li>Search</li></ul></div>
  <div class="col" style="left:347px"><h5>Help</h5><ul><li>Account</li><li>Addresses</li><li>Orders</li><li>Cart</li><li>Blog</li></ul></div>
  <div class="col contact" style="left:615px"><h5>Contact Us</h5><ul><li><b>T -</b>123.456.7890</li><li><b>P -</b>123.456.7890</li><li><b>E -</b>info@quintora.example</li></ul>
    <h5 class="hours">Opening Hours</h5><ul><li><strong>9 a.m to 12 a.m</strong> (Mon-Sat)</li><li><strong>9 a.m to 10 a.m</strong> (Mon-Sun)</li></ul></div>
  <div class="col" style="left:883px"><h5>Stay In the Know</h5><p class="note">Trust us, you'll want to hear what we have to say</p>
    <div class="email"><svg width="18" height="13" viewBox="0 0 18 13"><rect x="1" y="1" width="16" height="11" fill="#9a6366"/><path d="M1 1l8 6 8-6" fill="none" stroke="#fff" stroke-width="1.2"/></svg>Email</div>
    <a class="btn subscribe">SUBSCRIBE</a></div>
</footer>

<div class="bottombar">
  <span>Copyright © <strong>QUINTORA JEWELLERS</strong> - 2018 . All Right reserved</span>
  <div class="icons"><span></span><span></span><span></span><span></span><span></span></div>
</div>

</body>
</html>
```